Zielgruppe
TECHNIKVERLEIH
EVENTMANAGEMENT
BETRIEBSSICHERHEIT
VERANSTALTUNGSSERVICE
SOLAR
Aufgabenstellung
Texte anhand der 'auftrag_o42unpfuask7_lunoquart.pdf', Teaser Text für die Startseite selbst bestimmen, Farben anhand der Logos im Anhand und Ausgabe für Photoshop, XD oder PDF
Designt werden sollen die Startseite sowie eine Unterseite.

```html
<!DOCTYPE html>
<html lang="de">
<head>
<meta charset="utf-8">
<title>Lunoquart – Eventmanagement</title>
<link rel="stylesheet" href="https://fonts.googleapis.com/css2?family=Open+Sans:wght@300;400;600;700&display=swap">
<style>
  :root {
    --bg: #141414;
    --white: #ffffff;
    --lime: #b5c90a;
    --muted: #bdbdbd;
    --line: #8a8a8a;
  }
  * { margin: 0; padding: 0; box-sizing: border-box; }
  html, body { width: 1200px; height: 675px; overflow: hidden; background: var(--bg); }
  body { font-family: "Open Sans", sans-serif; color: var(--white); position: relative; }

  .hero-photo {
    position: absolute; inset: 0;
    background:
      radial-gradient(ellipse 320px 150px at 590px 215px, #f2f2f2 0%, #9a9a9a 30%, rgba(60,60,60,0.6) 65%, transparent 100%),
      radial-gradient(ellipse 700px 300px at 600px 200px, #4a4a4a 0%, #262626 60%, transparent 100%),
      linear-gradient(180deg, #1c1c1c 0%, #2a2a2a 40%, #1b1b1b 70%, #151515 100%);
  }

  .brand {
    position: absolute; left: 17px; top: 34px;
    display: flex; align-items: center; gap: 6px;
    font-weight: 600; font-size: 15px; letter-spacing: 0.5px;
  }
  .brand-mark { width: 10px; height: 10px; background: var(--lime); }

  .menu-toggle { position: absolute; right: 16px; top: 11px; }

  .hero-content { position: absolute; left: 184px; top: 278px; width: 820px; }
  .hero-title { font-weight: 400; font-size: 37px; line-height: 50px; letter-spacing: -0.3px; }
  .hero-title strong { color: var(--lime); font-weight: 700; }
  .hero-lead { margin-top: 38px; font-size: 18px; line-height: 25px; }

  .cta {
    position: absolute; left: 532px; top: 481px; width: 136px; height: 33px;
    background: var(--lime); color: #111; font-size: 18px;
    display: flex; align-items: center; justify-content: center;
  }

  .service-tabs {
    position: absolute; left: 205px; top: 614px; width: 780px;
    display: flex; font-size: 18px; color: var(--muted); font-weight: 300;
  }
  .service-tabs span { position: absolute; top: 0; white-space: nowrap; }
  .service-tabs .active { color: var(--white); font-weight: 700; }
  .tabs-rule { position: absolute; left: 218px; top: 650px; width: 750px; height: 1px; background: var(--line); }
  .tabs-indicator { position: absolute; left: 591px; top: 649px; width: 146px; height: 3px; background: var(--white); }
</style>
</head>
<body>
  <div class="hero-photo" role="img" aria-label="Konzertsaal in Schwarzweiß mit hellen Bühnenscheinwerfern und Publikum im Vordergrund"></div>

  <div class="brand"><span class="brand-mark"></span>LUNOQUART</div>

  <svg class="menu-toggle" width="20" height="20" viewBox="0 0 20 20" aria-label="Menü">
    <rect x="0" y="1" width="20" height="2" fill="#fff"/>
    <rect x="0" y="9" width="20" height="2" fill="#fff"/>
    <rect x="0" y="17" width="20" height="2" fill="#fff"/>
  </svg>

  <main class="hero-content">
    <h1 class="hero-title">Sie wollen eine Firmenfeier, einen Ball oder eine andere Festlichkeit <strong>veranstalten</strong>?</h1>
    <p class="hero-lead">Unsere kompetenten Eventmanager helfen Ihnen gern bei der Planung und Konzeption Ihrer Feierlichkeit.</p>
  </main>

  <a class="cta">Mehr erfahren</a>

  <nav class="service-tabs">
    <span style="left:0">VOLLER SERVICE</span>
    <span style="left:188px">TECHNIKVERLEIH</span>
    <span class="active" style="left:366px">EVENTMANAGEMENT</span>
    <span style="left:610px;top:-3px">BETRIEBSSICHERHEIT</span>
  </nav>
  <div class="tabs-rule"></div>
  <div class="tabs-indicator"></div>
</body>
</html>
```